Website Required for Small Cyber Security Company

Require a website for Cyber Security company. I have logo which i will attach. Please use logo blue and white as a guide
Would ultimately like the site to have a technology theme with the following pages Landing page
Services
Contact
Careers

I can provide content for each of those pages in due course, until then happy for you to use dummy data to display purposes

Target Market(s)

Government

Industry/Entity Type

Cyber Security

Coding

Coded - Design and coding required

Number of Pages Required

4 page

Colors
0054AA
0677BA
7BADD7
CADEEF
E8F1F8

Requirements
Must have
• High quality finish and UX
Nice to have
• look and feel professional and not cheap

```html
<!DOCTYPE html>
<html lang="en">
<head>
<meta charset="utf-8">
<title>Harrow Crest Consulting — Cybersecurity Services</title>
<link rel="stylesheet" href="https://fonts.googleapis.com/css2?family=Noto+Sans:wght@400;500;600;700&family=Roboto:wght@400;500;700&display=swap">
<style>
:root{
  --navy:#0d1a3a;
  --navy-deep:#08122b;
  --navy-card:#14224a;
  --ink:#1a2340;
  --teal:#0aa6cc;
  --teal-dark:#0677ba;
  --blue:#0054aa;
  --sky:#7badd7;
  --mist:#e8f1f8;
  --pale:#f4f6f9;
  --grey:#7a7f8c;
  --line:#d8dde6;
  --white:#ffffff;
  --black:#05070d;
  --star:#ff6a2b;
}
*{box-sizing:border-box;margin:0;padding:0}
html,body{width:1200px;height:4696px;overflow:hidden}
body{position:relative;background:var(--white);font-family:"Roboto",sans-serif;color:var(--ink)}
.abs{position:absolute}
.head{font-family:"Noto Sans",sans-serif}
.eyebrow{font-size:12px;letter-spacing:.3px;color:var(--teal);text-decoration:underline;text-underline-offset:4px;font-family:"Noto Sans",sans-serif}
.btn{display:flex;align-items:center;justify-content:center;gap:12px;background:var(--teal);color:var(--white);font-family:"Noto Sans",sans-serif;font-weight:600;font-size:15px;border-radius:3px}
.btn-pill{border-radius:22px;font-size:13px}
p.body{font-size:13px;line-height:21px;color:var(--grey)}

/* top bar */
.topbar{left:0;top:0;width:1200px;height:40px;background:var(--navy-deep);z-index:3;color:#c7cfe0;font-size:12px}
.topbar .item{top:12px;display:flex;align-items:center;gap:8px}
.topbar .sep{top:12px;width:1px;height:16px;background:#3a4666}
.topbar .soc{top:14px;width:10px;height:10px;border-radius:2px;background:#8794b3}

/* hero */
.hero{left:0;top:0;width:1200px;height:860px;overflow:hidden}
.hero-photo{left:0;top:0;width:1200px;height:860px;background:linear-gradient(135deg,#2b3448 0%,#1a2236 40%,#242c3d 70%,#141a28 100%)}
.hero-shade{left:0;top:0;width:1200px;height:860px;background:radial-gradient(ellipse at 50% 40%,rgba(30,40,62,.3),rgba(8,14,30,.7))}
.brand{display:flex;flex-direction:column;align-items:center;gap:4px;color:var(--white);font-family:"Noto Sans",sans-serif;font-weight:600}
.brand .dot{width:34px;height:34px;border-radius:50%;border:2px solid var(--white)}
.brand .name{font-size:11px;letter-spacing:.3px;white-space:nowrap}
.perk{display:flex;align-items:center;gap:12px;color:var(--white);font-family:"Noto Sans",sans-serif;font-weight:600;font-size:13px;line-height:16px}
.nav{left:93px;top:128px;width:1003px;height:67px;background:var(--white);z-index:2}
.nav a{position:absolute;top:24px;font-size:14px;color:var(--ink);text-decoration:none;font-family:"Noto Sans",sans-serif;font-weight:500;transform:translateX(-50%)}
.nav .active{top:0;height:67px;left:35px;width:92px;border-bottom:4px solid var(--teal)}
.hero-copy{left:0;width:1200px;text-align:center;color:var(--white)}

/* about */
.about-photo{left:100px;top:957px;width:438px;height:438px;border-radius:50%;background:linear-gradient(150deg,#9fb3c4,#5b6e82 45%,#2e3b55);border:10px solid var(--navy);border-top-color:#1c2b55}
.badge{left:435px;top:1288px;width:96px;height:96px;border-radius:50%;background:var(--white);box-shadow:0 6px 18px rgba(0,0,0,.15);display:flex;align-items:center;justify-content:center;flex-direction:column;gap:4px;font-family:"Noto Sans",sans-serif;font-weight:600;font-size:10px;color:var(--blue)}
.badge .dot{width:30px;height:30px;border-radius:50%;border:2px solid var(--blue)}

/* services */
.services{left:0;top:1440px;width:1200px;height:562px;background:var(--pale)}
.card{top:188px;width:316px;height:312px;background:var(--white);border:1px solid #e4e7ee;text-align:center}
.card h3{font-family:"Noto Sans",sans-serif;font-weight:500;font-size:19px;margin-top:12px}
.card p{font-size:13px;line-height:20px;color:#555c6a;margin-top:18px}
.card svg{margin-top:66px}
.card.feature{background:linear-gradient(160deg,#4a5366,#2a3350 55%,#1a2347);color:var(--white);border:none;border-bottom:4px solid var(--teal)}
.card.feature p{color:#e4e8f2}

/* cta */
.cta{left:0;top:2002px;width:1200px;height:306px;background:linear-gradient(120deg,#1b2131,#262d3d 50%,#161b28)}
.cta-box{left:350px;top:2277px;width:502px;height:57px;background:var(--white);box-shadow:0 8px 20px rgba(0,0,0,.12);display:flex;align-items:center;justify-content:space-around;font-size:15px;color:var(--ink);padding:0 20px;z-index:2}

/* why */
.why{left:0;top:2308px;width:1200px;height:660px;background:var(--pale)}
.why h4{font-family:"Noto Sans",sans-serif;font-weight:500;font-size:19px;color:var(--navy)}
.why .txt{font-size:13px;line-height:21px;color:var(--grey)}
.why .r{text-align:right}
.bubble{width:72px;height:72px;border-radius:50%;background:var(--white);box-shadow:0 6px 16px rgba(20,40,80,.1);display:flex;align-items:center;justify-content:center}

/* testimonials */
.testi{left:0;top:2968px;width:1200px;height:616px;background:linear-gradient(180deg,#141c30,#1f2840 50%,#111827)}
.tcard{top:213px;width:314px;height:270px;border:1px solid #3c4a78;background:var(--navy-card);color:var(--white);text-align:center}
.tcard.light{background:var(--white);color:var(--ink);border-color:#fff;border-bottom:5px solid var(--teal)}
.avatar{top:-36px;left:50%;margin-left:-34px;width:68px;height:68px;border-radius:50%;border:3px solid var(--white);background:linear-gradient(160deg,#c9b8a5,#6d5f55)}
.tcard .nm{font-size:15px;font-weight:500;margin-top:56px}
.tcard .stars{color:var(--star);font-size:15px;letter-spacing:2px;margin-top:2px}
.tcard p{font-size:12.5px;line-height:21px;margin:18px 28px 0}
.tcard.light p{color:#8a8f9b}
.tcard .q{font-family:"Noto Sans",sans-serif;font-weight:700;font-size:44px;line-height:44px;color:var(--teal);margin-top:12px}

/* contact */
.c-item{display:flex;gap:22px;align-items:flex-start}
.c-item b{display:block;font-size:12px;font-weight:700;color:var(--ink);letter-spacing:.2px}
.c-item span{font-size:12px;color:var(--grey);line-height:22px}
.form{left:602px;top:3659px;width:494px;height:567px;background:var(--white);border-top:4px solid var(--teal);box-shadow:0 4px 24px rgba(0,0,0,.08);z-index:4}
.form label{position:absolute;font-size:13px;font-weight:500;color:var(--ink)}
.field{position:absolute;height:42px;border:1px solid #c8ccd5;border-radius:21px;font-size:12px;color:#9aa0ab;padding:14px 24px}

/* footer */
.footer{left:0;top:4226px;width:1200px;height:470px;background:var(--black);color:#b9bdc8}
.footer h5{font-family:"Noto Sans",sans-serif;font-size:14px;font-weight:600;color:var(--white)}
.footer .link{font-size:12px;color:#b9bdc8;line-height:26px}
.sq{width:30px;height:30px;border-radius:3px;background:#3a3f6a}
.fc{display:flex;align-items:center;gap:14px}
.fc .ic{width:48px;height:48px;border-radius:50%;background:#3c3a5e;display:flex;align-items:center;justify-content:center}
.fc b{display:block;color:var(--white);font-size:13px;font-family:"Noto Sans",sans-serif;font-weight:600}
.fc span{font-size:11px;color:#9aa0ae}
</style>
</head>
<body>

<!-- Top bar -->
<div class="abs topbar">
  <div class="abs item" style="left:93px">
    <svg width="12" height="12" viewBox="0 0 24 24"><path d="M6.6 10.8a15 15 0 0 0 6.6 6.6l2.2-2.2a1 1 0 0 1 1-.25 11 11 0 0 0 3.6.6 1 1 0 0 1 1 1V20a1 1 0 0 1-1 1A17 17 0 0 1 3 4a1 1 0 0 1 1-1h3.5a1 1 0 0 1 1 1 11 11 0 0 0 .6 3.6 1 1 0 0 1-.25 1z" fill="#0aa6cc"/></svg>
    (+1) 234-567-890</div>
  <div class="abs sep" style="left:243px"></div>
  <div class="abs item" style="left:262px">
    <svg width="12" height="10" viewBox="0 0 24 18"><rect x="1" y="1" width="22" height="16" rx="2" fill="none" stroke="#0aa6cc" stroke-width="2"/><path d="M1 2l11 8 11-8" fill="none" stroke="#0aa6cc" stroke-width="2"/></svg>
    info@company.com</div>
  <div class="abs sep" style="left:412px"></div>
  <div class="abs item" style="left:432px">
    <svg width="10" height="13" viewBox="0 0 20 26"><path d="M10 1a8 8 0 0 1 8 8c0 6-8 15-8 15S2 15 2 9a8 8 0 0 1 8-8z" fill="#0aa6cc"/><circle cx="10" cy="9" r="3" fill="#08122b"/></svg>
    123 ABC DEF</div>
  <div class="abs soc" style="left:998px"></div>
  <div class="abs soc" style="left:1026px"></div>
  <div class="abs soc" style="left:1054px"></div>
  <div class="abs soc" style="left:1084px"></div>
</div>

<!-- Hero -->
<section class="abs hero">
  <div class="abs hero-photo" role="img" aria-label="Dark office photo of people working at laptops"></div>
  <div class="abs hero-shade"></div>

  <div class="abs brand" style="left:90px;top:52px"><div class="dot"></div><div class="name">HARROW CREST</div></div>
  <div class="abs perk" style="left:814px;top:68px">
    <svg width="26" height="26" viewBox="0 0 26 26"><circle cx="13" cy="13" r="11" fill="none" stroke="#0aa6cc" stroke-width="2"/><path d="M13 7v6l4 3" stroke="#0aa6cc" stroke-width="2" fill="none"/></svg>
    <div>24/7<br>Service</div></div>
  <div class="abs" style="left:947px;top:64px;width:1px;height:42px;background:#56607a"></div>
  <div class="abs perk" style="left:974px;top:68px">
    <svg width="26" height="26" viewBox="0 0 26 26"><path d="M4 12h4v11H4zM8 22h11l3-9h-7l1-6-3-2-5 7" fill="none" stroke="#0aa6cc" stroke-width="2" stroke-linejoin="round"/></svg>
    <div>Qualified<br>Professionals</div></div>

  <nav class="abs nav">
    <div class="abs active"></div>
    <a style="left:75px">Home</a>
    <a style="left:232px">About Us</a>
    <a style="left:369px">Services</a>
    <a style="left:511px">Blog</a>
    <a style="left:656px">Contact</a>
    <div class="abs btn btn-pill" style="left:823px;top:13px;width:154px;height:41px">Get A Quote</div>
  </nav>

  <div class="abs hero-copy head" style="top:372px;font-size:13px">CYBERSECURITY SERVICES</div>
  <h1 class="abs hero-copy head" style="top:398px;font-size:70px;line-height:76px;font-weight:500">Defending Your<br>Digital Frontier</h1>
  <div class="abs btn btn-pill" style="left:544px;top:623px;width:156px;height:38px">About Us</div>

  <svg class="abs" style="left:0;top:660px" width="1200" height="200" viewBox="0 0 1200 200">
    <path d="M0 24 C260 100 520 160 700 150 C900 140 1080 90 1200 38 L1200 200 L0 200 Z" fill="#fff"/>
    <path d="M137 79 C360 150 560 196 700 186 C880 174 1030 130 1122 88 C1030 150 860 205 690 196 C520 188 320 140 137 79 Z" fill="#0aa6cc"/>
    <path d="M137 79 C340 135 520 170 690 172 C860 170 1010 128 1122 88 C1020 138 860 186 690 186 C520 186 330 140 137 79 Z" fill="#0677ba" opacity=".55"/>
  </svg>
</section>

<!-- About -->
<div class="abs about-photo" role="img" aria-label="Photo of two colleagues reviewing a tablet"></div>
<div class="abs badge"><div class="dot"></div>HARROW CREST</div>

<div class="abs eyebrow" style="left:614px;top:966px">WHO WE ARE</div>
<h2 class="abs head" style="left:614px;top:998px;font-size:40px;line-height:52px;font-weight:600;color:var(--navy)">The team you can trust<br>to get the job done</h2>
<div class="abs head" style="left:614px;top:1132px;font-size:21px;font-weight:500;color:var(--navy)">Elevating Cybersecurity Excellence</div>
<p class="abs body" style="left:614px;top:1175px;width:506px">Lorem ipsum dolor sit amet, consectetur adipiscing elit, sed do eiusmod temp or incididunt ut labore et dolore magna aliqua. Ut enim ad minim veniam, quis laboris nisi ut aliquip ex ea commodo consequat.</p>
<p class="abs body" style="left:614px;top:1251px;width:506px">Lorem ipsum dolor sit amet, consectetur adipiscing elit, sed do eiusmod temp or incididunt ut labore et dolore magna aliqua.</p>
<div class="abs btn" style="left:613px;top:1333px;width:155px;height:45px">Contact us
  <svg width="18" height="12" viewBox="0 0 18 12"><path d="M0 6h16M11 1l5 5-5 5" stroke="#fff" stroke-width="2" fill="none"/></svg></div>

<!-- Services -->
<section class="abs services">
  <div class="abs eyebrow" style="left:0;width:1182px;text-align:center;top:50px">OUR SERVICES</div>
  <h2 class="abs head" style="left:0;width:1192px;text-align:center;top:82px;font-size:40px;font-weight:600;color:var(--navy)">Services We Offer</h2>

  <div class="abs card feature" style="left:93px" role="img" aria-label="Encryption services card over a photo of a person at a laptop">
    <svg width="54" height="54" viewBox="0 0 54 54" style="margin-top:70px"><path d="M14 42h26M18 42l6-14 10 4-4 10M24 28l4-10 8 2" fill="none" stroke="#fff" stroke-width="2.5" stroke-linejoin="round"/><circle cx="33" cy="14" r="5" fill="none" stroke="#fff" stroke-width="2.5"/></svg>
    <h3 style="margin-top:0">Encryption Services</h3>
    <p>Lorem ipsum dolor sit amet,<br>consectetur adipiscing<br>elit, sed do eiusmod tempor</p>
  </div>
  <div class="abs card" style="left:437px">
    <svg width="50" height="50" viewBox="0 0 50 50"><path d="M25 6a19 19 0 1 1-17 10" fill="none" stroke="#0aa6cc" stroke-width="2.5"/><path d="M4 10l4 7 7-4" fill="none" stroke="#0aa6cc" stroke-width="2.5"/><path d="M25 15c4 6 7 9 7 13a7 7 0 0 1-14 0c0-4 3-7 7-13z" fill="none" stroke="#0aa6cc" stroke-width="2.5"/></svg>
    <h3>Cloud Security</h3>
    <p>Lorem ipsum dolor sit amet,<br>consectetur adipiscing<br>elit, sed do eiusmod tempor</p>
  </div>
  <div class="abs card" style="left:781px">
    <svg width="54" height="54" viewBox="0 0 54 54" style="margin-top:60px"><path d="M27 8l17 12-6 20H16l-6-20z" fill="none" stroke="#0aa6cc" stroke-width="2.5" stroke-linejoin="round"/><circle cx="27" cy="8" r="4" fill="#fff" stroke="#0aa6cc" stroke-width="2.5"/><circle cx="44" cy="20" r="4" fill="#fff" stroke="#0aa6cc" stroke-width="2.5"/><circle cx="10" cy="20" r="4" fill="#fff" stroke="#0aa6cc" stroke-width="2.5"/><circle cx="38" cy="40" r="4" fill="#fff" stroke="#0aa6cc" stroke-width="2.5"/><circle cx="16" cy="40" r="4" fill="#fff" stroke="#0aa6cc" stroke-width="2.5"/></svg>
    <h3>Phishing Simulations</h3>
    <p>Lorem ipsum dolor sit amet,<br>consectetur adipiscing<br>elit, sed do eiusmod tempor</p>
  </div>
</section>

<!-- CTA -->
<section class="abs cta" role="img" aria-label="Dark photo of a busy office floor"></section>
<h2 class="abs head" style="left:0;width:1212px;text-align:center;top:2112px;font-size:31px;line-height:40px;font-weight:500;color:var(--white)">We're On <span style="color:var(--teal)">Call 24/7</span> to React Promptly to Your<br>Cybersecurity Needs</h2>
<div class="abs cta-box"><span>+ (001) 234-567-890</span><span>[or]</span><span>info@example.com</span></div>

<!-- Why choose us -->
<section class="abs why">
  <div class="abs eyebrow" style="left:0;width:1196px;text-align:center;top:80px">WHY CHOOSE US</div>
  <h2 class="abs head" style="left:0;width:1196px;text-align:center;top:113px;font-size:40px;font-weight:600;color:var(--navy)">Why Choose Us</h2>

  <div class="abs r" style="left:100px;width:263px;top:246px"><h4>Expertise &amp; Experience</h4><div class="txt">Lorem ipsum dolor sit amet,<br>consectetur adipiscing elit</div></div>
  <div class="abs r" style="left:80px;width:258px;top:365px"><h4>Research Capabilities</h4><div class="txt">Lorem ipsum dolor sit amet,<br>consectetur adipiscing elit</div></div>
  <div class="abs r" style="left:100px;width:263px;top:474px"><h4>Quality Assurance</h4><div class="txt">Lorem ipsum dolor sit amet,<br>consectetur adipiscing elit</div></div>
  <div class="abs" style="left:836px;top:246px"><h4>Customization</h4><div class="txt">Lorem ipsum dolor sit amet,<br>consectetur adipiscing elit</div></div>
  <div class="abs" style="left:874px;top:365px"><h4>Cost-Effective</h4><div class="txt">Lorem ipsum dolor sit amet,<br>consectetur adipiscing elit</div></div>
  <div class="abs" style="left:836px;top:474px"><h4>Client-Centric</h4><div class="txt">Lorem ipsum dolor sit amet,<br>consectetur adipiscing elit</div></div>

  <svg class="abs" style="left:398px;top:192px" width="400" height="400" viewBox="0 0 400 400">
    <defs><filter id="soft" x="-20%" y="-20%" width="140%" height="140%"><feDropShadow dx="0" dy="6" stdDeviation="10" flood-color="#1a2a55" flood-opacity=".12"/></filter></defs>
    <circle cx="200" cy="200" r="128" fill="none" stroke="#1b2456" stroke-width="3"/>
    <circle cx="200" cy="200" r="102" fill="#fff" filter="url(#soft)"/>
    <g fill="#fff" stroke="#1b2456" stroke-width="2.5">
      <circle cx="127" cy="97" r="7"/><circle cx="271" cy="97" r="7"/>
      <circle cx="72" cy="206" r="7"/><circle cx="328" cy="206" r="7"/>
      <circle cx="124" cy="312" r="7"/><circle cx="277" cy="312" r="7"/>
    </g>
    <circle cx="200" cy="176" r="18" fill="none" stroke="#0054aa" stroke-width="2.5"/>
    <text x="200" y="222" text-anchor="middle" font-family="Noto Sans, sans-serif" font-weight="600" font-size="15" fill="#0d1a3a">HARROW CREST</text>
    <text x="200" y="238" text-anchor="middle" font-family="Noto Sans, sans-serif" font-weight="600" font-size="9" letter-spacing="2" fill="#0d1a3a">CONSULTING</text>
  </svg>

  <div class="abs bubble" style="left:431px;top:241px"><svg width="28" height="28" viewBox="0 0 54 54"><path d="M14 42h26M18 42l6-14 10 4-4 10M24 28l4-10 8 2" fill="none" stroke="#0aa6cc" stroke-width="3"/><circle cx="33" cy="14" r="5" fill="none" stroke="#0aa6cc" stroke-width="3"/></svg></div>
  <div class="abs bubble" style="left:695px;top:241px"><svg width="28" height="28" viewBox="0 0 54 54"><path d="M14 42h26M18 42l6-14 10 4-4 10M24 28l4-10 8 2" fill="none" stroke="#0aa6cc" stroke-width="3"/><circle cx="33" cy="14" r="5" fill="none" stroke="#0aa6cc" stroke-width="3"/></svg></div>
  <div class="abs bubble" style="left:373px;top:353px"><svg width="28" height="28" viewBox="0 0 50 50"><path d="M25 6a19 19 0 1 1-17 10" fill="none" stroke="#0aa6cc" stroke-width="3"/><path d="M25 15c4 6 7 9 7 13a7 7 0 0 1-14 0c0-4 3-7 7-13z" fill="none" stroke="#0aa6cc" stroke-width="3"/></svg></div>
  <div class="abs bubble" style="left:752px;top:353px"><svg width="28" height="28" viewBox="0 0 50 50"><path d="M25 6a19 19 0 1 1-17 10" fill="none" stroke="#0aa6cc" stroke-width="3"/><path d="M25 15c4 6 7 9 7 13a7 7 0 0 1-14 0c0-4 3-7 7-13z" fill="none" stroke="#0aa6cc" stroke-width="3"/></svg></div>
  <div class="abs bubble" style="left:425px;top:458px"><svg width="28" height="28" viewBox="0 0 54 54"><path d="M27 8l17 12-6 20H16l-6-20z" fill="none" stroke="#0aa6cc" stroke-width="3" stroke-linejoin="round"/></svg></div>
  <div class="abs bubble" style="left:701px;top:458px"><svg width="28" height="28" viewBox="0 0 54 54"><path d="M27 8l17 12-6 20H16l-6-20z" fill="none" stroke="#0aa6cc" stroke-width="3" stroke-linejoin="round"/></svg></div>
</section>

<!-- Testimonials -->
<section class="abs testi" role="img" aria-label="Dark office photo backdrop">
</section>
<div class="abs head" style="left:0;width:1196px;text-align:center;top:3024px;font-size:13px;color:#d6dbe6;text-decoration:underline;text-underline-offset:4px">TESTIMONIALS</div>
<h2 class="abs head" style="left:0;width:1196px;text-align:center;top:3056px;font-size:40px;font-weight:500;color:var(--white)">What Clients are saying</h2>

<div class="abs tcard light" style="left:95px;top:3181px">
  <div class="abs avatar" role="img" aria-label="Client portrait"></div>
  <div class="nm">Owen Hale</div><div class="stars">★★★★★</div>
  <p>Lorem ipsum dolor sit amet, consectetur adip elit, sed do eiusmod tempor incididunt ut labore et dolore magna aliqua. Ut enim</p>
  <div class="q">“</div>
</div>
<div class="abs tcard" style="left:435px;top:3181px">
  <div class="abs avatar" role="img" aria-label="Client portrait" style="background:linear-gradient(160deg,#e3d3b8,#8a7a66)"></div>
  <div class="nm">Mara Quinn</div><div class="stars">★★★★★</div>
  <p>Lorem ipsum dolor sit amet, consectetur adip elit, sed do eiusmod tempor incididunt ut labore et dolore magna aliqua. Ut enim</p>
  <div class="q">“</div>
</div>
<div class="abs tcard" style="left:775px;top:3181px">
  <div class="abs avatar" role="img" aria-label="Client portrait" style="background:linear-gradient(160deg,#cfb49c,#6a5444)"></div>
  <div class="nm">Dev Sarin</div><div class="stars">★★★★★</div>
  <p>Lorem ipsum dolor sit amet, consectetur adip elit, sed do eiusmod tempor incididunt ut labore et dolore magna aliqua. Ut enim</p>
  <div class="q">“</div>
</div>
<svg class="abs" style="left:560px;top:3492px" width="64" height="14" viewBox="0 0 64 14"><circle cx="8" cy="7" r="4" fill="none" stroke="#aab3c8" stroke-width="1.5"/><rect x="20" y="6" width="22" height="2.5" rx="1" fill="#d6dbe6"/><circle cx="56" cy="7" r="4" fill="none" stroke="#aab3c8" stroke-width="1.5"/></svg>

<!-- Contact -->
<h2 class="abs head" style="left:108px;top:3642px;font-size:40px;color:var(--navy)"><span style="font-weight:600">Contact Us</span> <span style="font-weight:400">Today</span></h2>
<div class="abs c-item" style="left:112px;top:3730px">
  <svg width="52" height="40" viewBox="0 0 52 40"><circle cx="16" cy="22" r="15" fill="#e8f1f8"/><path d="M17 8a4 4 0 0 1 4 3l1 5-3 3a16 16 0 0 0 8 8l3-3 5 1a4 4 0 0 1 3 4v3a3 3 0 0 1-3 3A26 26 0 0 1 12 13a3 3 0 0 1 3-3z" fill="none" stroke="#0aa6cc" stroke-width="2"/></svg>
  <div><b>HEAD OFFICE</b><span>21 Lorem Ipsum, ABC 123</span></div></div>
<div class="abs c-item" style="left:112px;top:3805px">
  <svg width="52" height="40" viewBox="0 0 52 40"><circle cx="16" cy="22" r="15" fill="#e8f1f8"/><rect x="10" y="10" width="30" height="22" rx="2" fill="none" stroke="#0aa6cc" stroke-width="2"/><path d="M10 12l15 11 15-11M10 31l11-10M40 31L29 21" fill="none" stroke="#0aa6cc" stroke-width="2"/></svg>
  <div><b>EMAIL ADDRESS</b><span>name@company.com</span></div></div>
<div class="abs c-item" style="left:112px;top:3872px">
  <svg width="52" height="44" viewBox="0 0 52 44"><circle cx="16" cy="26" r="15" fill="#e8f1f8"/><path d="M25 4a10 10 0 0 1 10 10c0 8-10 20-10 20S15 22 15 14A10 10 0 0 1 25 4z" fill="none" stroke="#3cc46a" stroke-width="2"/><circle cx="25" cy="14" r="4" fill="none" stroke="#3cc46a" stroke-width="2"/></svg>
  <div><b>CALL US NOW</b><span>Call Now: 123-456-789</span></div></div>

<div class="abs form">
  <div class="abs head" style="left:38px;top:42px;font-size:24px;font-weight:500;color:var(--navy)">Send Us A Message</div>
  <label style="left:38px;top:112px">First Name</label>
  <div class="field" style="left:38px;top:133px;width:198px">John</div>
  <label style="left:251px;top:112px">Last Name</label>
  <div class="field" style="left:251px;top:133px;width:198px">Doe</div>
  <label style="left:38px;top:201px">Email</label>
  <div class="field" style="left:38px;top:221px;width:416px">info@company.com</div>
  <label style="left:38px;top:291px">Message</label>
  <div class="field" style="left:38px;top:310px;width:416px;height:124px;border-radius:3px">Type Your Message</div>
  <div class="abs btn" style="left:38px;top:471px;width:155px;height:44px">Contact us
    <svg width="18" height="12" viewBox="0 0 18 12"><path d="M0 6h16M11 1l5 5-5 5" stroke="#fff" stroke-width="2" fill="none"/></svg></div>
</div>

<!-- Footer -->
<svg class="abs" style="left:0;top:4070px" width="1200" height="160" viewBox="0 0 1200 160">
  <path d="M0 128 C140 80 360 58 602 64 L602 160 L0 160 Z" fill="#05070d"/>
  <path d="M86 138 C200 68 420 36 602 40 L602 60 C420 56 220 84 86 138 Z" fill="#0aa6cc"/>
  <path d="M1096 156 C1140 152 1175 146 1200 140 L1200 160 L1096 160 Z" fill="#05070d"/>
</svg>
<footer class="abs footer">
  <div class="abs brand" style="left:126px;top:22px"><div class="dot"></div><div class="name" style="font-size:15px">HARROW CREST</div><div class="name" style="font-size:9px;letter-spacing:2px">CONSULTING</div></div>
  <p class="abs" style="left:126px;top:130px;width:300px;font-size:11px;line-height:20px;color:#9aa0ae">Lorem ipsum dolor sit amet, consectetur adipiscing elit, sed do eiusmod tempor incididunt ut</p>
  <div class="abs sq" style="left:126px;top:196px;background:#0aa6cc"></div>
  <div class="abs sq" style="left:164px;top:196px"></div>
  <div class="abs sq" style="left:202px;top:196px"></div>
  <div class="abs sq" style="left:240px;top:196px"></div>

  <h5 class="abs" style="left:490px;top:48px">Quick Links</h5>
  <div class="abs link" style="left:490px;top:94px">Home<br>Services<br>About Us<br>Contact<br>Blog<br>Testimonials</div>
  <div class="abs link" style="left:625px;top:94px">Cookies Policy<br>Terms of Use<br>Careers<br>Our Team<br>More</div>

  <h5 class="abs" style="left:827px;top:48px">Newsletters</h5>
  <p class="abs" style="left:827px;top:94px;width:250px;font-size:11px;line-height:20px;color:#9aa0ae">Lorem ipsum dolor sit amet, consectetur adipiscing elit, sed do eiusmod tempor</p>
  <div class="abs" style="left:827px;top:151px;width:194px;height:46px;background:#fff;font-size:11px;color:#8a8f9b;padding:16px 24px">Enter Email Address</div>
  <div class="abs" style="left:1021px;top:151px;width:49px;height:46px;background:#0aa6cc;display:flex;align-items:center;justify-content:center"><svg width="12" height="16" viewBox="0 0 12 16"><path d="M2 2l7 6-7 6" stroke="#fff" stroke-width="3" fill="none"/></svg></div>

  <div class="abs fc" style="left:126px;top:292px"><div class="ic"><svg width="16" height="20" viewBox="0 0 20 26"><path d="M10 1a8 8 0 0 1 8 8c0 6-8 15-8 15S2 15 2 9a8 8 0 0 1 8-8z" fill="#8b7fd0"/><circle cx="10" cy="9" r="3" fill="#3c3a5e"/></svg></div><div><b>Address</b><span>123 Middle Street</span></div></div>
  <div class="abs fc" style="left:364px;top:292px"><div class="ic" style="background:#0aa6cc"><svg width="20" height="15" viewBox="0 0 24 18"><rect x="1" y="1" width="22" height="16" rx="2" fill="#fff"/><path d="M1 2l11 8 11-8" fill="none" stroke="#0aa6cc" stroke-width="2"/></svg></div><div><b>Email Us</b><span>support@harrowcrest.com</span></div></div>
  <div class="abs fc" style="left:631px;top:292px"><div class="ic"><svg width="16" height="16" viewBox="0 0 24 24"><path d="M6.6 10.8a15 15 0 0 0 6.6 6.6l2.2-2.2a1 1 0 0 1 1-.25 11 11 0 0 0 3.6.6 1 1 0 0 1 1 1V20a1 1 0 0 1-1 1A17 17 0 0 1 3 4a1 1 0 0 1 1-1h3.5a1 1 0 0 1 1 1 11 11 0 0 0 .6 3.6 1 1 0 0 1-.25 1z" fill="#8b7fd0"/></svg></div><div><b>Contact Us</b><span>+01(2)456) 789 99</span></div></div>
  <div class="abs fc" style="left:860px;top:292px"><div class="ic"><svg width="20" height="20" viewBox="0 0 26 26"><circle cx="13" cy="13" r="10" fill="none" stroke="#8b7fd0" stroke-width="2.5"/><path d="M13 8v5l3 3" stroke="#8b7fd0" stroke-width="2.5" fill="none"/></svg></div><div><b>Opening Hour</b><span>Mon - Friday 10 am - 8pm</span></div></div>

  <div class="abs" style="left:126px;top:404px;width:948px;height:1px;background:#2a2e3a"></div>
  <div class="abs head" style="left:0;width:1200px;text-align:center;top:436px;font-size:12px;font-weight:500;color:#fff">HARROW CREST CONSULTING</div>
</footer>

</body>
</html>
```